Beacon Guard Services

Our Company is a security business which needs a cut edge design, the final product should have all relevant information and maintain a bold but modern and professional look.

Target Market(s)

A cut edge design which will attract any audience

Industry/Entity Type

Security

Contact Information for Business Card

BEACON GUARD SERVICES

Daniel Hofstra
Operations Manager
Phone: 0412 739 215

Email: info@beaconguard.com.au
Web: www.beaconguard.com.au

Requirements
Must have
• Must be double sided and contain all relevant information and the company logo.

```html
<!DOCTYPE html>
<html lang="en">
<head>
<meta charset="utf-8">
<title>Beacon Guard Services – Business Card</title>
<link href="https://fonts.googleapis.com/css2?family=Michroma&display=swap" rel="stylesheet">
<style>
  :root {
    --backdrop: #2a2a2c;
    --teal-deep: #1f3a43;
    --teal-mid: #2f5560;
    --teal-light: #4f7a84;
    --orange: #f28a1e;
    --orange-bright: #f7a631;
    --paper: #ffffff;
    --paper-shade: #e4e6e7;
    --ink-dark: #2a424a;
    --text-light: #f2f5f6;
  }
  * { box-sizing: border-box; margin: 0; padding: 0; }
  html, body {
    width: 1200px; height: 900px; overflow: hidden;
    background: var(--backdrop);
    font-family: "Michroma", "Arial", sans-serif;
  }
  .canvas { position: relative; width: 1200px; height: 900px; }

  .card {
    position: absolute; width: 640px; height: 366px; overflow: hidden;
    box-shadow: 0 18px 40px rgba(0,0,0,.55);
  }

  /* Front side */
  .card-front { left: 80px; top: 60px; background: var(--teal-deep); }
  .front-header {
    position: absolute; left: 0; top: 0; width: 100%; height: 200px;
    background: linear-gradient(120deg, var(--paper) 45%, var(--paper-shade) 100%);
  }
  .header-glow {
    position: absolute; right: 0; top: 0; width: 260px; height: 200px;
    background: radial-gradient(circle at 60% 55%, rgba(247,166,49,.35), rgba(255,255,255,0) 65%);
  }
  .accent-band {
    position: absolute; left: 0; top: 200px; width: 100%; height: 7px;
    background: linear-gradient(90deg, var(--orange), var(--orange-bright));
  }
  .accent-pointer {
    position: absolute; left: 64px; top: 207px; width: 0; height: 0;
    border-left: 12px solid transparent; border-right: 12px solid transparent;
    border-top: 12px solid var(--orange);
  }
  .front-body {
    position: absolute; left: 0; top: 207px; width: 100%; height: 159px;
    background: linear-gradient(180deg, var(--teal-mid), var(--teal-deep));
  }
  .brand {
    position: absolute; display: flex; align-items: center; gap: 18px;
  }
  .brand-mark { width: 58px; height: 58px; background: var(--orange); }
  .brand-name { font-size: 38px; letter-spacing: 1px; color: var(--ink-dark); line-height: 1; }
  .card-front .brand { left: 40px; top: 70px; }

  .person { position: absolute; left: 40px; top: 268px; }
  .person-name { font-size: 19px; color: var(--orange); letter-spacing: 1px; }
  .person-role { margin-top: 8px; font-size: 10px; color: var(--text-light); letter-spacing: 1px; }

  .contacts { position: absolute; left: 360px; top: 226px; list-style: none; }
  .contacts li {
    display: flex; align-items: center; gap: 10px;
    font-size: 10px; color: var(--text-light); margin-bottom: 10px; letter-spacing: .5px;
  }
  .contacts svg { width: 12px; height: 12px; flex: none; }

  /* Back side */
  .card-back {
    left: 480px; top: 474px;
    background: radial-gradient(circle at 50% 40%, var(--teal-light) 0%, var(--teal-mid) 40%, var(--teal-deep) 100%);
  }
  .card-back .brand {
    left: 0; top: 120px; width: 100%; justify-content: center;
  }
  .card-back .brand-name { color: var(--text-light); font-size: 40px; }
  .back-web {
    position: absolute; left: 0; top: 262px; width: 100%; text-align: center;
    font-size: 12px; letter-spacing: 5px; color: var(--text-light);
  }
</style>
</head>
<body>
<main class="canvas">

  <section class="card card-front" aria-label="Business card front">
    <div class="front-header">
      <div class="header-glow"></div>
      <div class="brand">
        <span class="brand-mark"></span>
        <span class="brand-name">BEACON GUARD</span>
      </div>
    </div>
    <div class="front-body"></div>
    <div class="accent-band"></div>
    <div class="accent-pointer"></div>

    <div class="person">
      <p class="person-name">DANIEL HOFSTRA</p>
      <p class="person-role">OPERATIONS MANAGER</p>
    </div>

    <ul class="contacts">
      <li>
        <svg viewBox="0 0 12 12" aria-hidden="true"><rect x="3" y="0.5" width="6" height="11" rx="1.2" fill="none" stroke="#f28a1e" stroke-width="1.3"/><circle cx="6" cy="9.5" r=".8" fill="#f28a1e"/></svg>
        0412 739 215
      </li>
      <li>
        <svg viewBox="0 0 12 12" aria-hidden="true"><rect x=".7" y="2.5" width="10.6" height="7" fill="none" stroke="#f28a1e" stroke-width="1.3"/><path d="M1 3l5 3.5L11 3" fill="none" stroke="#f28a1e" stroke-width="1.2"/></svg>
        INFO@BEACONGUARD.COM.AU
      </li>
      <li>
        <svg viewBox="0 0 12 12" aria-hidden="true"><circle cx="6" cy="6" r="5" fill="none" stroke="#f28a1e" stroke-width="1.3"/><path d="M1 6h10M6 1c-2.5 3-2.5 7 0 10M6 1c2.5 3 2.5 7 0 10" fill="none" stroke="#f28a1e" stroke-width="1"/></svg>
        WWW.BEACONGUARD.COM.AU
      </li>
    </ul>
  </section>

  <section class="card card-back" aria-label="Business card back">
    <div class="brand">
      <span class="brand-mark"></span>
      <span class="brand-name">BEACON GUARD</span>
    </div>
    <p class="back-web">WWW.BEACONGUARD.COM.AU</p>
  </section>

</main>
</body>
</html>
```